Velmora Flowers Florist Flyer

We are requiring a flyer that advertises and promotes our new business. We specialise in weddings and events but would also like to branch out to corporates and an online subscription. Our brand is feminine/romantic with a touch of elegance and luxury. Our main colour schemes are white, black, gold and pale pink. Instagram: Velmora_flowers and website www.velmoraflowers.com.au
Target Market(s)
brides to be, females
Industry/Entity Type
Florist
Font styles to use
Sans Serif
Script
Other font styles liked:
- The Carpenter
Colors
ffffff
000000
333333
Requirements
Must have
- Feminine/romantic feel, through use of theme colours and elegant font
- our contact details Ph: 0478215096
- email address: contactus@velmoraflowers.com.au
Nice to have
- a description of us willing to work with clients to create their dream wedding flowers. That we offer consultations and no obligation quotes.

```html
<!DOCTYPE html>
<html lang="en">
<head>
<meta charset="utf-8">
<title>Velmora Flowers – Flyer</title>
<link href="https://fonts.googleapis.com/css2?family=Great+Vibes&family=Cormorant+Garamond:wght@400;500&family=Crimson+Text:ital,wght@0,400;1,400;1,700&display=swap" rel="stylesheet">
<style>
  :root{
    --backdrop:#d4d4d4;
    --ink:#111111;
    --charcoal:#333333;
    --paper:#ffffff;
    --blush:#e9a9c9;
    --blush-soft:#fbf3f7;
    --quote-pink:#e58fbb;
    --gold-dark:#8a6420;
    --gold:#c9a24a;
    --gold-light:#f0d78a;
  }
  *{box-sizing:border-box;margin:0;padding:0}
  html,body{width:1200px;height:1200px;overflow:hidden;background:var(--backdrop)}
  .flyer{
    position:absolute;left:216px;top:62px;width:767px;height:1076px;
    background:linear-gradient(180deg,var(--paper) 60%,var(--blush-soft) 100%);
    overflow:hidden;font-family:"Crimson Text",Georgia,serif;color:var(--ink);
  }
  .flyer__art{position:absolute;left:0;top:0;width:767px;height:680px}
  .brand{
    position:absolute;left:0;width:767px;text-align:center;color:var(--paper);
    font-family:"Cormorant Garamond",Georgia,serif;font-weight:400;line-height:1;
  }
  .brand__name{top:62px;font-size:48px;letter-spacing:10px;padding-left:10px}
  .brand__sub{top:136px;font-size:16px;letter-spacing:18px;padding-left:18px}
  .headline{
    position:absolute;top:650px;left:0;width:767px;height:96px;text-align:center;
    font-family:"Great Vibes",cursive;font-weight:400;font-size:70px;line-height:96px;
    background:linear-gradient(180deg,var(--gold-light) 20%,var(--gold) 50%,var(--gold-dark) 85%);
    -webkit-background-clip:text;background-clip:text;color:transparent;
  }
  .tagline{
    position:absolute;top:740px;left:0;width:767px;text-align:center;
    font-style:italic;font-size:19px;line-height:24px;color:var(--charcoal);
  }
  .quote{
    position:absolute;left:84px;top:774px;width:600px;height:64px;
    border:2.5px solid var(--gold);border-radius:22px;
    text-align:center;font-style:italic;font-weight:700;font-size:17.5px;line-height:24px;
    padding-top:6px;color:var(--ink);
  }
  .quote__mark{position:absolute;font-family:Georgia,serif;color:var(--quote-pink);font-size:34px;font-weight:400;font-style:normal;line-height:1}
  .quote__mark--open{left:10px;top:-12px}
  .quote__mark--close{right:-14px;bottom:-22px}
  .quote__author{position:absolute;right:32px;bottom:6px;font-size:12px;font-weight:400;font-style:normal;letter-spacing:.3px}
  .about__title{position:absolute;left:46px;top:852px;font-style:italic;font-weight:700;font-size:19px;line-height:24px}
  .about__col{
    position:absolute;top:879px;width:322px;font-style:italic;font-size:12.6px;line-height:16.2px;
    text-align:justify;color:var(--charcoal);
  }
  .about__col--left{left:48px}
  .about__col--right{left:398px}
  .offer{
    position:absolute;top:955px;left:0;width:767px;text-align:center;
    font-style:italic;font-weight:700;font-size:21px;line-height:28px;
  }
  .contact{
    position:absolute;left:46px;top:1000px;width:676px;height:35px;border-radius:12px;
    background:var(--blush);display:flex;align-items:center;padding:0 14px;
    font-size:12.8px;color:var(--ink);
  }
  .contact__item{display:flex;align-items:center;gap:8px}
  .contact__item + .contact__item{margin-left:26px}
  .contact__icon{width:18px;height:18px;flex:none}
  .contact__social{display:flex;gap:10px;margin-left:26px}
</style>
</head>
<body>
<main class="flyer">
  <svg class="flyer__art" viewBox="0 0 767 680" xmlns="http://www.w3.org/2000/svg">
    <defs>
      <linearGradient id="venueTone" x1="0" y1="0" x2="0" y2="1">
        <stop offset="0" stop-color="#8f8a7c"/>
        <stop offset=".35" stop-color="#a9b3ad"/>
        <stop offset=".55" stop-color="#6f6a4e"/>
        <stop offset="1" stop-color="#3a2a22"/>
      </linearGradient>
      <linearGradient id="bouquetMixed" x1="0" y1="0" x2="1" y2="1">
        <stop offset="0" stop-color="#6d7a3b"/><stop offset=".5" stop-color="#c94a4a"/><stop offset="1" stop-color="#3e5a2c"/>
      </linearGradient>
      <linearGradient id="bouquetWhite" x1="0" y1="0" x2="1" y2="1">
        <stop offset="0" stop-color="#e9e3d6"/><stop offset=".6" stop-color="#d9cfc4"/><stop offset="1" stop-color="#6e7a66"/>
      </linearGradient>
      <linearGradient id="bouquetRed" x1="0" y1="0" x2="1" y2="1">
        <stop offset="0" stop-color="#7a1f24"/><stop offset=".6" stop-color="#d9c2b4"/><stop offset="1" stop-color="#3f5a2e"/>
      </linearGradient>
      <linearGradient id="tableTone" x1="0" y1="0" x2="0" y2="1">
        <stop offset="0" stop-color="#c9b79a"/><stop offset="1" stop-color="#eeeae2"/>
      </linearGradient>
    </defs>
    <polygon class="art__band" fill="var(--ink)" points="0,0 767,0 767,170 632,38 384,282 136,38 0,170"/>
    <g role="img" aria-label="Photo of a candlelit wedding reception hall with long tables, floral centrepieces and a country view">
      <polygon fill="url(#venueTone)" points="0,170 136,38 384,282 632,38 767,170 767,450 744,426 624,542 504,420 384,534 264,414 144,534 0,434"/>
    </g>
    <g stroke="#ffffff" stroke-opacity=".55" stroke-width="1" fill="none">
      <line x1="20" y1="180" x2="264" y2="414"/>
      <line x1="250" y1="170" x2="40" y2="380"/>
      <line x1="747" y1="180" x2="504" y2="414"/>
      <line x1="517" y1="170" x2="727" y2="380"/>
    </g>
    <g role="img" aria-label="Photo of a long banquet table with tall white floral arrangements">
      <polygon fill="url(#tableTone)" points="0,434 144,546 0,670"/>
    </g>
    <g role="img" aria-label="Photo of a mixed bouquet with red roses, anthurium and greenery">
      <polygon fill="url(#bouquetMixed)" points="264,414 384,534 264,654 144,534"/>
    </g>
    <g role="img" aria-label="Photo of a white and blush rose bouquet">
      <polygon fill="url(#bouquetWhite)" points="504,420 624,542 504,654 384,534"/>
    </g>
    <g role="img" aria-label="Photo of deep red and cream roses arrangement">
      <polygon fill="url(#bouquetRed)" points="744,426 767,450 767,646 744,670 624,542"/>
    </g>
  </svg>

  <div class="brand brand__name">VELMORA</div>
  <div class="brand brand__sub">FLOWERS</div>

  <h1 class="headline">Velmora Flower</h1>
  <p class="tagline">Creating stunning Flowers for Weddings and Events</p>

  <blockquote class="quote">
    <span class="quote__mark quote__mark--open">&ldquo;</span>
    Design is not making beauty, beauty emerges from selection,<br>affinities, integration, love.
    <span class="quote__author">- LENA MARWICK</span>
    <span class="quote__mark quote__mark--close">&rdquo;</span>
  </blockquote>

  <h2 class="about__title">About Us:</h2>
  <p class="about__col about__col--left">For generations we've been creating flowers for family and friends. Over the years this has been our test bed for creating our design pieces for weddings and events. Now we want to make our beautiful creations available to everyone.</p>
  <p class="about__col about__col--right">Our designers have had extensive backgrounds, from owning a florist, to chocolate bouquet design and creations. Our friends and family loved working with our designers to create their perfect flower design, no matter what the event was</p>

  <p class="offer">~&nbsp; We offer consultations &amp; no obligation quotes &nbsp;~</p>

  <footer class="contact">
    <span class="contact__item">
      <svg class="contact__icon" viewBox="0 0 18 18"><rect x="3" y="3" width="12" height="12" transform="rotate(45 9 9)" fill="var(--ink)"/><path d="M6.6 6.2l1.3-.4.8 1.6-.8.6c.4.9 1 1.5 1.9 1.9l.6-.8 1.6.8-.4 1.3c-2.6-.2-4.8-2.4-5-5z" fill="var(--paper)"/></svg>
      +61 4 782 150 96
    </span>
    <span class="contact__item">
      <svg class="contact__icon" viewBox="0 0 18 18"><rect x="3" y="3" width="12" height="12" transform="rotate(45 9 9)" fill="var(--ink)"/><rect x="6" y="6.8" width="6" height="4.4" fill="none" stroke="var(--paper)" stroke-width=".9"/><path d="M6 6.8l3 2.4 3-2.4" fill="none" stroke="var(--paper)" stroke-width=".9"/></svg>
      contactus@velmoraflowers.com.au
    </span>
    <span class="contact__item">
      <svg class="contact__icon" viewBox="0 0 18 18"><rect x="3" y="3" width="12" height="12" transform="rotate(45 9 9)" fill="var(--ink)"/><circle cx="9" cy="9" r="3.2" fill="none" stroke="var(--paper)" stroke-width=".9"/><path d="M5.8 9h6.4M9 5.8c-1.6 2-1.6 4.4 0 6.4M9 5.8c1.6 2 1.6 4.4 0 6.4" fill="none" stroke="var(--paper)" stroke-width=".7"/></svg>
      www.velmoraflowers.com.au
    </span>
    <span class="contact__social" aria-label="Social media">
      <svg class="contact__icon" viewBox="0 0 18 18"><rect x="3" y="3" width="12" height="12" transform="rotate(45 9 9)" fill="var(--ink)"/></svg>
      <svg class="contact__icon" viewBox="0 0 18 18"><rect x="3" y="3" width="12" height="12" transform="rotate(45 9 9)" fill="var(--ink)"/></svg>
      <svg class="contact__icon" viewBox="0 0 18 18"><rect x="3" y="3" width="12" height="12" transform="rotate(45 9 9)" fill="var(--ink)"/></svg>
    </span>
  </footer>
</main>
</body>
</html>
```